Web SITE design for new book

I need a unique design for a book my friend is releasing.

The home page needs to include:
A picture of the book
A spot for a video

Navigation:
Home
About the Book
Buy the Book
About the Author
Investing
Log In

The person awarded the project will also need to provide designs for the 5 other internal pages. They should be pretty straight forward.

Link to book design: https://www.crestlocker.example/s/qwv82ntzr3kfbjm/book-cover.png

Thanks!

```html
<!DOCTYPE html>
<html lang="en">
<head>
<meta charset="utf-8">
<title>Five Pitfalls Every Investor Should Dodge</title>
<link href="https://fonts.googleapis.com/css2?family=Open+Sans:wght@400;600;700&family=Mulish:wght@400&display=swap" rel="stylesheet">
<style>
:root{
  --gold:#9b8133;
  --nav-active:#4a4d52;
  --ink:#333;
  --ink-soft:#555;
  --muted:#666;
  --page:#eeeeee;
  --hero:#ebebeb;
  --white:#ffffff;
  --rule:#d8d8d8;
  --alert:#e8151b;
  --player:#1c1c1c;
}
*{box-sizing:border-box;margin:0;padding:0}
html,body{width:1200px;height:1128px;overflow:hidden}
body{font-family:"Open Sans",Arial,sans-serif;background:var(--page);color:var(--ink);position:relative}
a{color:inherit;text-decoration:none}

.topnav{position:absolute;top:0;left:0;width:1200px;height:40px;background:var(--gold)}
.topnav ul{position:absolute;left:248px;top:0;display:flex;list-style:none;height:40px}
.topnav li a{display:block;height:40px;line-height:40px;padding:0 10px;color:var(--white);font-size:13.5px}
.topnav li.active a{background:var(--nav-active)}
.topnav .social{position:absolute;left:872px;top:0;height:40px;display:flex;gap:10px;align-items:center;font-size:11px;color:var(--white);font-weight:600}

.masthead{position:absolute;top:40px;left:0;width:1200px;height:104px;border-bottom:1px solid var(--rule)}
.brand{position:absolute;left:258px;top:28px;display:flex;align-items:center;gap:12px}
.brand .mark{width:44px;height:44px;border-radius:50%;background:var(--gold)}
.brand .name{font-size:35px;font-weight:700;color:#444;letter-spacing:-0.3px}
.phone{position:absolute;right:258px;top:42px;font-size:16px;color:var(--ink-soft)}

.hero{position:absolute;top:145px;left:0;width:1200px;height:513px;background:var(--hero);border-bottom:1px solid var(--rule)}
.hero .pitch{position:absolute;left:264px;top:167px;width:340px;text-align:center;font-family:"Mulish",sans-serif;font-size:24px;line-height:26.5px;color:#3a3a3a}
.btn-buy{position:absolute;left:354px;top:270px;width:162px;height:35px;border-radius:18px;background:var(--gold);color:var(--white);font-size:16px;line-height:35px;text-align:center}
.cover{position:absolute;left:648px;top:55px;width:290px;height:416px;background:linear-gradient(160deg,#ffffff 0%,#f2f2f2 60%,#dcdcdc 100%);border-right:8px solid #222;box-shadow:0 10px 18px rgba(0,0,0,.25);transform:skewY(4deg)}

.feature{position:absolute;top:659px;left:0;width:1200px;height:293px;background:var(--white);border-bottom:1px solid var(--rule)}
.video{position:absolute;left:258px;top:19px;width:320px;height:250px;background:var(--player)}
.video .frame{height:213px;background:linear-gradient(135deg,#eee6d8 0%,#e9dcc6 45%,#cfc4b4 100%)}
.video svg{display:block}
.copy{position:absolute;left:603px;top:35px;width:340px}
.copy h2{font-weight:400;font-size:24px;line-height:28px;color:var(--gold);padding-bottom:14px;border-bottom:1.5px solid var(--gold)}
.copy p{margin-top:14px;font-size:12.6px;line-height:16px;color:#222;letter-spacing:-0.05px}
.btn-more{display:block;margin-top:8px;width:78px;height:17px;background:var(--alert);color:var(--white);font-size:10px;line-height:17px;text-align:center}

.footer{position:absolute;top:953px;left:0;width:1200px;text-align:center;color:var(--muted)}
.footer .links{margin-top:39px;font-size:10px}
.footer .links span{margin:0 4px}
.footer .copyright{margin-top:10px;font-size:10px}
.footer .social{margin-top:16px;font-size:11px;font-weight:600;color:#999}
.footer .social a{margin:0 6px}
</style>
</head>
<body>

<nav class="topnav">
  <ul>
    <li><a href="#">Home</a></li>
    <li class="active"><a href="#">About the Book</a></li>
    <li><a href="#">Buy the Book</a></li>
    <li><a href="#">About the Author</a></li>
    <li><a href="#">Investing</a></li>
    <li><a href="#">LogIn</a></li>
  </ul>
  <div class="social"><a href="#">Friendsheet</a><a href="#">Chirper</a></div>
</nav>

<header class="masthead">
  <div class="brand"><span class="mark"></span><span class="name">Logo Here</span></div>
  <div class="phone">Call Us : 1800 555 010</div>
</header>

<section class="hero">
  <p class="pitch">Lorem ipsum dolor sit amet, adipiscing elit. Sed dolor non augue pretium.</p>
  <a class="btn-buy" href="#">Buy this Book</a>
  <div class="cover" role="img" aria-label="Book cover: Five Pitfalls Every Investor Should Dodge"></div>
</section>

<section class="feature">
  <div class="video">
    <div class="frame" role="img" aria-label="Video still: a hand stacking coins"></div>
    <svg width="320" height="37" viewBox="0 0 320 37">
      <circle cx="21" cy="18.5" r="11" fill="#fff"/>
      <path d="M18 13 L26 18.5 L18 24 Z" fill="#1c1c1c"/>
      <rect x="41" y="13" width="180" height="10" fill="#bdbdbd"/>
      <rect x="41" y="13" width="75" height="10" fill="#9b8133"/>
      <rect x="104" y="0" width="18" height="10" fill="#fff"/>
      <text x="113" y="8" font-size="7" text-anchor="middle" fill="#000" font-family="Open Sans,sans-serif">1:45</text>
      <text x="228" y="21.5" font-size="8" fill="#fff" font-family="Open Sans,sans-serif">01:15:45</text>
      <path d="M269 15 h4 l5 -4 v15 l-5 -4 h-4 Z" fill="#fff"/>
      <path d="M281 14 q3 4.5 0 9 M284 12 q5 6.5 0 13" stroke="#fff" stroke-width="1.3" fill="none"/>
      <path d="M296 13 h4 M296 13 v4 M308 13 h-4 M308 13 v4 M296 24 h4 M296 24 v-4 M308 24 h-4 M308 24 v-4" stroke="#fff" stroke-width="2"/>
    </svg>
  </div>
  <div class="copy">
    <h2>Learn how improve<br>mistake for good invetment</h2>
    <p>Lorem ipsum dolor sit amet, consectetur adipiscing elit. In fermentum dolor non augue pretium egestas. Donec sem eros, tincidunt at congue ut, posuere sit amet est. Vivamus scelerisque viverra odio sit amet laoreet. Ut nec neque non justo rutrum tempor lobortis eu ante. Aliquam sagittis, nibh quis commodo auctor</p>
    <a class="btn-more" href="#">Click Here</a>
  </div>
</section>

<footer class="footer">
  <div class="links">
    <a href="#">Home</a><span>/</span><a href="#">About the Book</a><span>/</span><a href="#">Buy the Book</a><span>/</span><a href="#">About the Author</a><span>/</span><a href="#">Investing</a><span>/</span><a href="#">Login</a><span>/</span><a href="#">Terms</a>
  </div>
  <div class="copyright">Copyright © 2014</div>
  <div class="social"><a href="#">Friendsheet</a><a href="#">Chirper</a></div>
</footer>

</body>
</html>
```